Consulting group
Business cards and stationary
Use same font as used in my logo
I think it is Swiss721?
Simple
Damon Fairley
President
417 W. Marlow Avenue, Apt 118 Dunmore, OR 97338
Damon@DamonFairley.com
www.TheCopperLantern.com
Looking for envelope, letterhead, and business card.
the logo? if you want to try putting a quote on it: "“The worst thing that can happen to a good cause is, not to be skillfully attacked, but to be ineptly defended.” - Corvelle. Not sure if I will like the quote on there or not.

```html
<!DOCTYPE html>
<html lang="en">
<head>
<meta charset="utf-8">
<title>The Copper Lantern – Business Card</title>
<link href="https://fonts.googleapis.com/css2?family=Arimo:wght@400;700&display=swap" rel="stylesheet">
<style>
  :root {
    --red: #e8242b;
    --ink: #1a1a1a;
    --grey: #555555;
    --paper: #ffffff;
    --backdrop: #e9e7e4;
    --rule: #9a9a9a;
  }
  * { box-sizing: border-box; margin: 0; padding: 0; }
  html, body {
    width: 1200px; height: 914px; overflow: hidden;
    background: var(--backdrop);
    font-family: "Arimo", Helvetica, Arial, sans-serif;
  }
  .canvas {
    width: 1200px; height: 914px;
    display: flex; align-items: center; justify-content: center;
  }
  .card {
    width: 1000px; height: 572px;
    background: var(--paper);
    border: 26px solid var(--red);
    position: relative;
    box-shadow: 0 6px 24px rgba(0,0,0,0.12);
  }
  .brand {
    position: absolute; top: 62px; left: 50%;
    transform: translateX(-50%);
    display: flex; align-items: flex-start; gap: 18px;
  }
  .brand-square {
    width: 86px; height: 86px; background: var(--red); margin-top: 6px;
  }
  .brand-name {
    font-weight: 700; font-size: 40px; line-height: 1.0;
    color: var(--ink); letter-spacing: -0.5px;
  }
  .person {
    position: absolute; top: 252px; left: 0; right: 0; text-align: center;
  }
  .person-name { color: var(--red); font-weight: 700; font-size: 22px; }
  .person-title { color: var(--grey); font-size: 17px; margin-top: 4px; }
  .details {
    position: absolute; top: 318px; left: 0; right: 0;
    display: flex; justify-content: center;
  }
  .address {
    width: 300px; text-align: right; padding-right: 20px; padding-top: 4px;
    color: var(--grey); font-size: 17px; line-height: 1.45; font-style: normal;
  }
  .divider { width: 1px; height: 140px; background: var(--rule); }
  .contacts { width: 320px; padding-left: 18px; list-style: none; }
  .contacts li {
    display: flex; align-items: center; gap: 10px;
    color: var(--grey); font-size: 17px; height: 29px;
  }
  .contacts svg { width: 20px; height: 20px; flex: none; }
</style>
</head>
<body>
<main class="canvas">
  <section class="card">
    <div class="brand">
      <div class="brand-square"></div>
      <div class="brand-name">The<br>Copper<br>Lantern</div>
    </div>

    <div class="person">
      <p class="person-name">Damon Fairley</p>
      <p class="person-title">President</p>
    </div>

    <div class="details">
      <address class="address">
        417 W. Marlow Avenue, Apt 118<br>Dunmore, OR 97338
      </address>
      <div class="divider"></div>
      <ul class="contacts">
        <li>
          <svg viewBox="0 0 20 20"><circle cx="10" cy="10" r="10" fill="var(--red)"/><path d="M6.5 5.5 L8.5 5.5 L9.2 8 L8 9 Q9 11.2 11 12 L12 10.8 L14.5 11.5 L14.5 13.5 Q9.5 14 6.5 8.5 Z" fill="#fff"/></svg>
          720.555.0143
        </li>
        <li>
          <svg viewBox="0 0 20 20"><circle cx="10" cy="10" r="10" fill="var(--red)"/><path d="M6.5 5.5 L8.5 5.5 L9.2 8 L8 9 Q9 11.2 11 12 L12 10.8 L14.5 11.5 L14.5 13.5 Q9.5 14 6.5 8.5 Z" fill="#fff"/></svg>
          808.555.0187
        </li>
        <li>
          <svg viewBox="0 0 20 20"><circle cx="10" cy="10" r="10" fill="var(--red)"/><rect x="5" y="6.5" width="10" height="7" fill="#fff"/><path d="M5 6.5 L10 10.5 L15 6.5" fill="none" stroke="var(--red)" stroke-width="1"/></svg>
          Damon@DamonFairley.com
        </li>
        <li>
          <svg viewBox="0 0 20 20"><circle cx="10" cy="10" r="10" fill="var(--red)"/><circle cx="10" cy="10" r="5" fill="none" stroke="#fff" stroke-width="1.2"/><ellipse cx="10" cy="10" rx="2.2" ry="5" fill="none" stroke="#fff" stroke-width="1"/><line x1="5" y1="10" x2="15" y2="10" stroke="#fff" stroke-width="1"/></svg>
          www.TheCopperLantern.com
        </li>
      </ul>
    </div>
  </section>
</main>
</body>
</html>
```